verdant terraces simple classy business card design

my name is owen harlow and I run a gardening business aimed at high class verdant terraces. the business name is verdant terraces and our logo was designed on pixel forum .My clientel are anything from residential homes to businesses. I take pride in my work and know that I offer a service like no other in my area.
The business card will be used to represent my business and I want it to be not only rememberable, but simplistic and modern. Eye catching too. Of course I would like it relatable to gardening and appealing to the correct clientel - those being garden enthusiasts, prestigious homes and businesses that are after top of the line gardening services like no other on the market.
I am not a typical lawn mowing business so I don't want a typical card design that represents that. The gardens I work with are generally million dollar properties with owners who are very garden proud looking for upkeep and guidance from me along with sometimes whole new garden designs. I want the business cards to show to my clients that I take pride, as they do, in their garden. And I want them to know from my card that I am a professional, qualified horticulturist offering them a top of the line service for life. I want them to refer my business on. I want them to look at my business card and see class and professionalism in a modern unique bold way.
The card should be simple with the possibility of the logo on the front being embossed/debossed and my details on the back the card should have a organic garden feel it's very important to me that it is absolutely perfect
I am also very open to ideas and suggestions so look forward to seeing the designs. the business logo has been supplied with this project and I want the card to be double sided

Contact info is
Owen Harlow - Managing Director / Horticulturist
Phone : 0481 526 704
Email: owenharlow@verdantterraces.com.au

Target Market(s)

high class gardens residential and commercial

Industry/Entity Type

Gardener

Contact Information for Business Card

Contact info is
Phone : 0481 526 704

PLEASE MAKE CARD DOUBLE SIDED

Requirements
Must have
• organic simple classy modern feel
• must flow with the current logo that has been supplied with this project
• Double sided
• Must explain in a simple way that I deal with high end gardens and I'm a qualified horticulturist
Nice to have
• embossed debossed logo
Should not have
• shouldn't be to busy or cheap looking

```html
<!DOCTYPE html>
<html lang="en">
<head>
<meta charset="utf-8">
<title>Verdant Terraces — Business Card</title>
<link href="https://fonts.googleapis.com/css2?family=Cinzel:wght@500;600&family=Open+Sans:wght@600&display=swap" rel="stylesheet">
<style>
  :root {
    --bg: #e4e6e4;
    --green-bright: #3c9c36;
    --green-mid: #2a7a2c;
    --green-deep: #123a16;
    --green-ink: #2f7d2f;
    --text-dark: #1c1c1c;
    --paper: #ffffff;
  }
  html, body {
    margin: 0;
    width: 1200px;
    height: 1200px;
    overflow: hidden;
    background: var(--bg);
  }
  .canvas {
    position: relative;
    width: 1200px;
    height: 1200px;
  }
  .card {
    position: absolute;
    left: 150px;
    width: 900px;
    height: 514px;
    overflow: hidden;
    box-shadow: 0 10px 28px rgba(0,0,0,0.18);
  }
  /* Front side */
  .card--front {
    top: 60px;
    background: linear-gradient(180deg, var(--green-bright) 0%, var(--green-mid) 35%, var(--green-deep) 100%);
  }
  .card--front .foliage {
    position: absolute;
    right: 0;
    top: 0;
    width: 400px;
    height: 514px;
    border-radius: 180px 0 0 220px;
    background: radial-gradient(circle at 60% 45%, #2e7a2a 0%, #1e5a1f 45%, #f4f7f3 46%, #ffffff 100%);
  }
  .wordmark {
    position: absolute;
    left: 64px;
    bottom: 70px;
    font-family: "Cinzel", serif;
    font-weight: 600;
    color: var(--paper);
    font-size: 46px;
    line-height: 1.1;
  }
  .wordmark span { display: block; }
  .wordmark .wordmark__sub { letter-spacing: 0.55em; font-size: 30px; }

  /* Back side */
  .card--back {
    top: 626px;
    background: var(--paper);
  }
  .card--back .foliage {
    position: absolute;
    left: 0;
    top: 0;
    width: 330px;
    height: 514px;
    border-radius: 0 200px 160px 0;
    background: radial-gradient(circle at 40% 45%, #ffffff 0%, #e6f1e4 30%, #4aa246 31%, #2f8a2f 100%);
  }
  .details {
    position: absolute;
    left: 380px;
    top: 70px;
    right: 50px;
  }
  .details__brand {
    font-family: "Cinzel", serif;
    font-weight: 600;
    color: var(--green-ink);
    font-size: 38px;
    line-height: 1.1;
    margin: 0;
  }
  .details__brand span { display: block; }
  .details__brand .sub { letter-spacing: 0.5em; font-size: 24px; }
  .details__rule {
    border: 0;
    border-top: 2px solid var(--green-ink);
    margin: 28px 0 24px;
  }
  .details__name {
    font-family: "Cinzel", serif;
    font-weight: 500;
    color: var(--green-ink);
    font-size: 40px;
    letter-spacing: 0.04em;
    margin: 0 0 4px;
  }
  .details__role,
  .contact {
    font-family: "Open Sans", sans-serif;
    font-weight: 600;
    color: var(--text-dark);
  }
  .details__role { font-size: 22px; margin: 0 0 26px; }
  .contact { list-style: none; padding: 0; margin: 0; font-size: 22px; }
  .contact li { display: flex; align-items: center; gap: 14px; margin-bottom: 12px; }
  .contact svg { width: 22px; height: 22px; fill: var(--green-ink); flex: none; }
</style>
</head>
<body>
<main class="canvas">
  <section class="card card--front" aria-label="Card front">
    <div class="foliage" role="img" aria-label="Stylised leafy tree canopy illustration in greens on white"></div>
    <p class="wordmark"><span>Verdant</span><span class="wordmark__sub">Terraces</span></p>
  </section>

  <section class="card card--back" aria-label="Card back">
    <div class="foliage" role="img" aria-label="Stylised white leaves on a green canopy illustration"></div>
    <div class="details">
      <p class="details__brand"><span>Verdant</span><span class="sub">Terraces</span></p>
      <hr class="details__rule">
      <h1 class="details__name">OWEN HARLOW</h1>
      <p class="details__role">Managing Director / Horticulturist</p>
      <ul class="contact">
        <li>
          <svg viewBox="0 0 24 24" aria-hidden="true"><path d="M6.6 10.8a15.1 15.1 0 0 0 6.6 6.6l2.2-2.2a1 1 0 0 1 1-.25 11.4 11.4 0 0 0 3.6.57 1 1 0 0 1 1 1V20a1 1 0 0 1-1 1A17 17 0 0 1 3 4a1 1 0 0 1 1-1h3.5a1 1 0 0 1 1 1 11.4 11.4 0 0 0 .57 3.6 1 1 0 0 1-.25 1z"/></svg>
          <span>0481 526 704</span>
        </li>
        <li>
          <svg viewBox="0 0 24 24" aria-hidden="true"><path d="M2 5h20v14H2z M2 5l10 8 10-8" /></svg>
          <span>owenharlow@verdantterraces.com.au</span>
        </li>
      </ul>
    </div>
  </section>
</main>
</body>
</html>
```